Webdesign für IT-Beratungsdienstleister
Zielgruppe
7K-ADVISA ist spezialisiert auf Fach- und IT-Beratungsdienstleistungen.
Wir unterstützen Unternehmen bei der Leistungsoptimierung durch prozessgetriebene Informationssysteme und Integrationslösungen.
Bitte siehe Aufgaben hier: http://www.7k-advisa.example/ueber-uns/
Zielgruppe sind Mittelständige und sowie Grossunternehmen
Aufgabenstellung
Wordpress template, modern, nicht zu überladen mit der Möglichkeit Beiträge zu veröffentlicehn. Responsive.

```html
<!DOCTYPE html>
<html lang="de">
<head>
<meta charset="utf-8">
<title>7K-ADVISA – Kontakt</title>
<link rel="stylesheet" href="https://fonts.googleapis.com/css2?family=Ubuntu:wght@300;400;500;700&display=swap">
<style>
:root{
  --accent:#e8630a;
  --rule:#e2261c;
  --text:#4a4a4a;
  --muted:#8a8a8a;
  --line:#d9d9d9;
  --footer:#262e3a;
  --white:#ffffff;
}
*{margin:0;padding:0;box-sizing:border-box}
html,body{width:953px;height:1200px;overflow:hidden;background:var(--white)}
body{position:relative;font-family:'Ubuntu',sans-serif;color:var(--text)}
.abs{position:absolute}
.brand{left:191px;top:12px;font-size:22px;font-weight:400;color:#333;letter-spacing:.5px;display:flex;align-items:center;gap:6px}
.brand .dot{width:14px;height:14px;border-radius:50%;background:var(--accent)}
.nav{top:18px;right:191px;display:flex;gap:14px;font-size:8.8px;font-weight:300;color:#555;align-items:center}
.nav .active{border:1px solid var(--accent);color:var(--accent);padding:3px 6px}
.hero{left:0;top:50px;width:953px;height:158px;background:linear-gradient(100deg,#c9c9cb 0%,#b9b5b3 40%,#c79a82 65%,#8a837f 100%)}
.hero-title{left:191px;top:96px;font-size:19px;font-weight:700;color:var(--white)}
.hero-rule{left:191px;top:125px;width:25px;height:2px;background:var(--rule)}
.h2{font-size:12.5px;font-weight:400;color:#444}
.rule{width:25px;height:2px;background:var(--rule)}
.photo{left:191px;top:298px;width:91px;height:125px;background:linear-gradient(180deg,#ec6a10 0%,#e5600a 55%,#3a3a3f 100%)}
.row{display:flex;align-items:center;gap:6px;font-size:8px;font-weight:300;color:#444;left:191px}
.row svg{width:9px;height:9px;fill:var(--accent);flex:none}
.bio{left:191px;top:478px;width:275px;font-size:7.4px;line-height:12.5px;font-weight:300;color:#444}
.field{left:484px;width:278px;height:26px;border:1px solid var(--line);border-radius:2px;padding:3px 4px}
.field b{display:block;font-size:4.6px;font-weight:500;color:#777;letter-spacing:.2px}
.field span{display:block;font-size:6.2px;color:#9a9a9a;margin-top:3px}
.btn{left:484px;top:697px;width:43px;height:20px;background:var(--accent);color:var(--white);font-size:6.5px;font-weight:700;display:flex;align-items:center;justify-content:center}
.map{left:0;top:754px;width:953px;height:251px;background:linear-gradient(120deg,#f7efe8 0%,#fbc9a6 35%,#f9b88c 60%,#f7efe8 100%)}
.footer{left:0;top:1005px;width:953px;height:195px;background:var(--footer)}
.f-brand{left:191px;top:1033px;font-size:17px;color:var(--white);display:flex;align-items:center;gap:5px}
.f-brand .dot{width:11px;height:11px;border-radius:50%;background:var(--white)}
.f-text{left:191px;top:1072px;width:222px;font-size:5.6px;line-height:12.5px;font-weight:500;color:var(--white)}
.f-head{font-size:9px;font-weight:700;color:var(--white)}
.f-links{left:435px;top:1050px;font-size:5.8px;font-weight:500;color:var(--white);line-height:12.5px;list-style:none}
.social{left:636px;width:14px;height:14px;background:#0d0f12}
.f-rule{left:191px;top:1149px;width:571px;height:2px;background:var(--rule)}
.copy{left:0;width:953px;top:1168px;text-align:center;font-size:7.6px;font-weight:300;color:#aab}
.copy strong{color:var(--white);font-weight:500}
</style>
</head>
<body>
<header>
  <div class="abs brand"><span>7K-ADVISA</span><span class="dot"></span></div>
  <nav class="abs nav">
    <span>Home</span><span>Über Uns</span><span>Business Consulting</span><span>IT Consulting</span><span>Training</span><span class="active">Kontakt</span>
  </nav>
</header>

<div class="abs hero" role="img" aria-label="Foto: Hände auf einer Laptop-Tastatur"></div>
<h1 class="abs hero-title">Kontakt</h1>
<div class="abs hero-rule"></div>

<section>
  <h2 class="abs h2" style="left:191px;top:258px">Profil</h2>
  <div class="abs rule" style="left:191px;top:283px"></div>
  <div class="abs photo" role="img" aria-label="Porträtfoto des Beraters vor orangem Hintergrund"></div>

  <div class="abs row" style="top:442px"><svg viewBox="0 0 10 10"><circle cx="5" cy="3" r="2.4"/><path d="M0.5 10c0-3 2-4.5 4.5-4.5S9.5 7 9.5 10z"/></svg>Dr. Kalen Obuya</div>
  <div class="abs row" style="top:458px"><svg viewBox="0 0 10 10"><path d="M3.5 1h3v1.5h3V9H.5V2.5h3zM4.3 1.8v.7h1.4v-.7z"/></svg>Senior Consultant at 7K-ADVISA</div>

  <p class="abs bio">Diplom Informatiker der Hochschule Wendenau und promovierter Wirtschaftsingenieur an der Elite Hochschule Ecole Supérieure de Valmont (Frankreich) und der technischen Universität Corvelle (ITV). Promotion zum Thema ganzheitliches Geschäftsprozessmanagement und Risikomanagement als Ansatz zur Optimierung der Unternehmensleistung. Erfahrener Business &amp; IT Berater.</p>

  <h2 class="abs h2" style="left:191px;top:551px">Kontaktdaten</h2>
  <div class="abs rule" style="left:191px;top:577px"></div>

  <div class="abs row" style="top:596px;font-weight:700"><svg viewBox="0 0 10 10"><path d="M5 .5L.5 3h9zM1 3.6h8v.8H1zM1.5 4.8h1.2v3.4H1.5zM4.4 4.8h1.2v3.4H4.4zM7.3 4.8h1.2v3.4H7.3zM.5 8.6h9v1H.5z"/></svg>7K-ADVISA Dr. Obuya</div>
  <div class="abs row" style="top:619px"><svg viewBox="0 0 10 10"><path d="M5 .3A3.4 3.4 0 0 0 1.6 3.7C1.6 6.3 5 9.8 5 9.8s3.4-3.5 3.4-6.1A3.4 3.4 0 0 0 5 .3zm0 4.8a1.4 1.4 0 1 1 0-2.8 1.4 1.4 0 0 1 0 2.8z"/></svg>Birkenweg 14</div>
  <div class="abs row" style="top:632px;left:193px">70999 Talheim</div>
  <div class="abs row" style="top:646px;left:193px">Deutschland</div>
  <div class="abs row" style="top:662px"><svg viewBox="0 0 10 10"><path d="M2.2.6l1.6 2-1 1.2a6 6 0 0 0 3.4 3.4l1.2-1 2 1.6-1 1.6C4.5 9.2.8 5.5 1 1.6z"/></svg>+49 700 55501200</div>
  <div class="abs row" style="top:678px"><svg viewBox="0 0 10 10"><path d="M2.8.3h4.4v9.4H2.8zm.9 1v6.4h2.6V1.3zM5 8.2a.5.5 0 1 0 0 1 .5.5 0 0 0 0-1z"/></svg>+49 150 55 01 234</div>
  <div class="abs row" style="top:694px"><svg viewBox="0 0 10 10"><path d="M.5 2h9v6h-9zM1.2 2.6L5 5.6l3.8-3z" /></svg>info(@)7k-advisa.example</div>
  <div class="abs row" style="top:710px"><svg viewBox="0 0 10 10"><path d="M.5 1.5h9v5.6h-9zm1 1v3.6h7V2.5zM3.5 8h3v1h-3z"/></svg>http://www.7k-advisa.example</div>
</section>

<section>
  <h2 class="abs h2" style="left:484px;top:258px">Kontaktformular</h2>
  <div class="abs rule" style="left:484px;top:283px"></div>

  <div class="abs field" style="top:303px"><b>VORNAME*</b><span>Geben Sie bitte Ihren Vornamen ein</span></div>
  <div class="abs field" style="top:337px"><b>NACHNAME*</b><span>Geben Sie bitte Ihren Nachnamen ein</span></div>
  <div class="abs field" style="top:370px"><b>E-MAIL*</b><span>Geben Sie bitte Ihre E-Mail Adresse ein</span></div>
  <div class="abs field" style="top:404px"><b>TELEFON</b><span>Geben Sie bitte Ihre Telefonnummer ein</span></div>
  <div class="abs field" style="top:437px"><b>FIRMA</b><span>Geben Sie bitte Ihre Firma ein</span></div>
  <div class="abs field" style="top:471px"><b>BETREFF*</b><span>Geben Sie bitte den Betreff ein</span></div>
  <div class="abs field" style="top:505px;height:174px"><b>NACHRICHT*</b><span>Geben Sie bitte Ihre Nachricht ein</span></div>
  <div class="abs btn">Senden</div>
</section>

<div class="abs map" role="img" aria-label="Stadtplan mit Standortmarkierung des Büros"></div>

<footer>
  <div class="abs footer"></div>
  <div class="abs f-brand"><span>7K-ADVISA</span><span class="dot"></span></div>
  <p class="abs f-text">Lorem ipsum dolor sit amet, consetetur sadipscing elitr, sed diam nonumy eirmod tempor invidunt ut labore et dolore magna aliquyam erat, sed diam voluptua. At vero eos et accusam et justo duo dolores et ea rebum.</p>

  <div class="abs f-head" style="left:435px;top:1031px">Links</div>
  <ul class="abs f-links">
    <li>Home</li><li>Über Uns</li><li>Business Consulting</li><li>IT Consulting</li><li>Training</li><li>Kontakt</li>
  </ul>

  <div class="abs f-head" style="left:630px;top:1031px">Soziale Netzwerke</div>
  <div class="abs social" style="top:1047px"></div>
  <div class="abs social" style="top:1065px"></div>
  <div class="abs social" style="top:1083px"></div>
  <div class="abs social" style="top:1100px"></div>
  <div class="abs social" style="top:1118px"></div>

  <div class="abs f-rule"></div>
  <p class="abs copy">Copyright © 2016 7K-ADVISA. | <strong>Home</strong> | <strong>Impressum</strong> | <strong>Kontakt</strong></p>
</footer>
</body>
</html>
```